Nirel Solutions Business Card
Stationary as well/logo for resumes, etc.
We are getting there. I need two samples...I like the black face Quorvix has going. I want the website across the bottom. I potentially want to see a black fade into a white bottom (background).
I also don't want it too busy so one color (blue) font. quorvix is close to what I am seeking
Gang,
I uploaded the files of my logo and am sorry for doing this late. What I am looking for is a business card and staionary that incorporates this. Peltcraft you are close to what I am lookign for witht he staionary- the card layout, I like tobrenik's better. In my logo there is a two tone as well, some with a black background and some with white- i want to try and explore this...

```html
<!DOCTYPE html>
<html lang="en">
<head>
<meta charset="utf-8">
<title>Nirel Solutions Stationery</title>
<link rel="stylesheet" href="https://fonts.googleapis.com/css2?family=Roboto:wght@400;500;700;900&display=swap">
<style>
  :root {
    --stage: #2c2c2c;
    --paper: #ffffff;
    --card-dark: #262626;
    --card-mid: #3a3a3a;
    --brand-blue: #2fb3d6;
    --brand-blue-deep: #136f8c;
    --ink-light: #f2f2f2;
    --ink-muted: #c9c9c9;
    --orb: #9ea3a8;
  }
  * { box-sizing: border-box; margin: 0; padding: 0; }
  html, body { width: 1200px; height: 910px; overflow: hidden; }
  body {
    position: relative;
    background: var(--stage);
    font-family: "Roboto", Arial, sans-serif;
  }

  .brand { display: flex; align-items: center; gap: 12px; }
  .brand-dot { border-radius: 50%; background: var(--orb); flex: none; }
  .brand-name { font-weight: 700; color: var(--brand-blue); letter-spacing: 0.04em; line-height: 1; }

  /* Letterhead */
  .letterhead {
    position: absolute; left: 258px; top: 25px; width: 657px; height: 848px;
    background: var(--paper);
  }
  .letterhead .brand { position: absolute; left: 32px; top: 38px; }
  .letterhead .brand-dot { width: 84px; height: 84px; }
  .letterhead .brand-name { font-size: 30px; }
  .letterhead-contact {
    position: absolute; right: 18px; top: 24px;
    color: var(--brand-blue); font-size: 14px; line-height: 17px;
  }
  .contact-grid { display: grid; grid-template-columns: auto auto auto; column-gap: 8px; }
  .letterhead-web { text-align: right; margin-top: 10px; }

  /* Business card back */
  .card-info {
    position: absolute; left: 59px; top: 360px; width: 462px; height: 270px;
    background: linear-gradient(180deg, var(--card-mid), var(--card-dark));
    color: var(--ink-light);
  }
  .card-info .person { position: absolute; left: 22px; top: 22px; }
  .person-name { font-size: 15px; font-weight: 700; }
  .person-title { font-size: 9px; color: var(--ink-muted); margin-top: 2px; }
  .card-info .address { position: absolute; left: 22px; top: 78px; font-size: 10px; line-height: 14px; }
  .card-info .numbers {
    position: absolute; left: 22px; top: 138px; font-size: 10px; line-height: 14px;
    display: grid; grid-template-columns: 42px auto; column-gap: 4px;
  }
  .card-info .brand { position: absolute; right: 22px; top: 70px; flex-direction: column; gap: 10px; }
  .card-info .brand-dot { width: 90px; height: 90px; }
  .card-info .brand-name { font-size: 20px; text-align: center; }
  .web-band {
    position: absolute; left: 0; right: 0; bottom: 14px; height: 30px;
    background: linear-gradient(90deg, var(--brand-blue-deep), var(--brand-blue) 50%, var(--brand-blue-deep));
    display: flex; align-items: center; justify-content: center;
    color: var(--ink-light); font-weight: 700; font-size: 13px; letter-spacing: 0.04em;
  }

  /* Business card front */
  .card-front {
    position: absolute; left: 600px; top: 350px; width: 410px; height: 235px;
    background: linear-gradient(180deg, var(--card-dark), var(--card-mid));
    color: var(--ink-light);
  }
  .card-front .front-orb {
    position: absolute; left: 190px; top: 26px; width: 170px; height: 170px;
    border-radius: 50%; background: radial-gradient(circle at 40% 35%, #b9bdc1, #5c6064);
  }
  .tagline {
    position: absolute; left: 28px; top: 42px;
    font-size: 34px; font-weight: 900; line-height: 40px; text-align: center;
  }
  .card-front .brand-name {
    position: absolute; left: 150px; top: 170px; font-size: 26px;
  }

  /* Envelope */
  .envelope {
    position: absolute; left: 345px; top: 640px; width: 725px; height: 230px;
    background: linear-gradient(180deg, var(--card-mid), var(--card-dark));
    color: var(--ink-light);
  }
  .envelope .brand { position: absolute; left: 22px; top: 22px; }
  .envelope .brand-dot { width: 64px; height: 64px; }
  .envelope .brand-name { font-size: 22px; }
  .envelope .address {
    position: absolute; left: 400px; top: 20px; font-size: 17px; line-height: 21px; font-style: normal;
  }
  .envelope .web-band { bottom: 14px; height: 54px; font-size: 26px; }
</style>
</head>
<body>

  <section class="letterhead" aria-label="Letterhead">
    <div class="brand">
      <span class="brand-dot"></span>
      <span class="brand-name">NIREL SOLUTIONS</span>
    </div>
    <div class="letterhead-contact">
      <div class="contact-grid">
        <span>Phone</span><span>:</span><span>555.204.6130</span>
        <span>Cell</span><span>:</span><span>555.204.6131</span>
        <span>Fax</span><span>:</span><span>555.204.6132</span>
      </div>
      <div class="letterhead-web">E-mail : dorian@nirel-it.com<br>www.nirel-it.com</div>
    </div>
  </section>

  <section class="card-info" aria-label="Business card, contact side">
    <div class="person">
      <div class="person-name">Dorian K. Halvesby</div>
      <div class="person-title">Business Development Manager</div>
    </div>
    <address class="address" style="font-style:normal">
      1840 Harlow Crest Drive<br>Suite 200<br>Fairmont, TX 77390
    </address>
    <div class="numbers">
      <span>Phone</span><span>: 555.204.6130</span>
      <span>Cell</span><span>: 555.204.6131</span>
      <span>Fax</span><span>: 555.204.6132</span>
      <span>E-mail</span><span>: dorian@nirel-it.com</span>
    </div>
    <div class="brand">
      <span class="brand-dot"></span>
      <span class="brand-name">NIREL SOLUTIONS</span>
    </div>
    <div class="web-band">www.nirel-it.com</div>
  </section>

  <section class="card-front" aria-label="Business card, front">
    <span class="front-orb"></span>
    <div class="tagline">Saving<br>Your<br>Business</div>
    <span class="brand-name">NIREL SOLUTIONS</span>
  </section>

  <section class="envelope" aria-label="Envelope">
    <div class="brand">
      <span class="brand-dot"></span>
      <span class="brand-name">NIREL SOLUTIONS</span>
    </div>
    <address class="address">
      1840 Harlow Crest Drive<br>Suite 200<br>Fairmont, TX 77390
    </address>
    <div class="web-band">www.nirel-it.com</div>
  </section>

</body>
</html>
```